Urgent * Legal Consultant Website Design

Provide a brief overview about your business Hello, website design required for independent legal consultant. Upload your company logo in the brief UPLOADED Specify the main navigation menu of your website (For better reference here's a sample of a website's navigation menu: (http://brovik88.net/wp-content/uploads/2012/css-menu/ 3.jpg) Header menu should include: About Us, Our people, Services and Contact Us Indicate the subpages or the dropdown menu if you have any (Refer to: http://pemtaz.co/wp-content/uploads/2010 /11/nav.jpg) No Subpages in the dropdown Upload to separate file for the text or the content needed for the homepage (This is a helpful supporting file to provide in order for our designers to better understand the elements needed on how to layout your This could be in Word document if you're using Windows or in Pages if you are using Mac. ) GET your legal advice and protect you and your BUSINESS Family Law Debt Recovery Leases Crimes & Traffic, wills Violence Restraining Orders Probate Titles Shariah Law Provide some samples of Web designs you like for better reference (Cite 2 to 3 samples) Website must be clean , simple and display our services in a clear way. Examples: https://cdn.vurdomix.com/wp/wp-content/uploads/sites/2/trosmo-simple-business-wordpress-theme-1024x846.jpg https://cdn.vurdomix.com/wp/wp -content / uploads / sites / 2 / pelinor-creative-studio-wp-website-template-1024x791.jpg Upload photos or files you would like to include in the design, or make mention if you are open to use stock photos Open to Use stock photos
Number of Pages Required
1 page
Look and feel
Each slider illustrates characteristics of the customer's brand and the style your logo design should communicate.

```html
<!DOCTYPE html>
<html lang="en">
<head>
<meta charset="utf-8">
<title>Lexmore Counsel</title>
<link href="https://fonts.googleapis.com/css2?family=Montserrat:wght@400;500;600;700&family=Lato:wght@400;700&display=swap" rel="stylesheet">
<style>
:root{
  --ink:#111;
  --black:#000;
  --gold:#f4d675;
  --cream:#fdf8e6;
  --card:#fdf6e1;
  --muted:#777;
  --body:#333;
  --bar:#3b3b3b;
  --white:#fff;
}
*{margin:0;padding:0;box-sizing:border-box}
html,body{width:1200px;height:2937px;overflow:hidden}
body{position:relative;background:var(--white);font-family:'Lato',sans-serif;color:var(--body)}
.abs{position:absolute}
.brand{font-family:'Montserrat',sans-serif;font-weight:700;letter-spacing:.5px}

/* header */
.site-header{left:0;top:0;width:1200px;height:135px;background:var(--white)}
.site-header .brand{left:74px;top:56px;font-size:24px;color:var(--ink)}
.main-nav{right:75px;top:60px;display:flex;gap:34px;align-items:center}
.main-nav a{font-family:'Montserrat',sans-serif;font-size:13px;font-weight:500;color:var(--ink);text-decoration:none}
.main-nav a.active{background:var(--black);color:var(--gold);padding:3px 10px;border-radius:10px}

/* hero */
.hero{left:0;top:135px;width:1200px;height:573px;background:linear-gradient(180deg,#8c8f94 0%,#7d8187 50%,#6f7277 100%)}
.hero-title{left:0;top:218px;width:1200px;text-align:center;font-family:'Montserrat',sans-serif;font-weight:700;font-size:43px;line-height:52px;color:var(--white)}
.hero-sub{left:0;top:328px;width:1200px;text-align:center;font-size:21px;color:var(--white)}
.hero-arrow{top:260px}

/* about */
.about-photo{left:110px;top:788px;width:460px;height:307px;background:linear-gradient(135deg,#9ea3ab,#6b7079)}
.about-text{left:605px;top:783px;width:495px}
h2{font-family:'Montserrat',sans-serif;font-weight:700;color:var(--ink)}
.about-text h2{font-size:27px;margin-bottom:12px}
.about-text p{font-size:13px;line-height:16.5px;color:#555;text-align:justify;margin-bottom:16px}
.btn-more{display:inline-block;background:var(--black);color:var(--gold);font-family:'Montserrat',sans-serif;font-size:11px;font-weight:600;padding:3px 10px;border-radius:10px}

/* people */
.people{left:0;top:1170px;width:1200px;height:602px;background:var(--cream)}
.section-title{width:1200px;left:0;text-align:center;font-size:27px}
.section-lead{left:100px;width:1000px;text-align:center;font-size:13px;line-height:17.5px;color:#444}
.person{width:287px;text-align:center}
.person .photo{width:287px;height:287px}
.person .name{margin-top:20px;font-family:'Montserrat',sans-serif;font-size:16px;font-weight:600;color:#333}
.person .role{margin-top:2px;font-size:13px;color:var(--muted)}

/* practice */
.area{width:222px;height:258px;background:var(--card);text-align:center;padding-top:38px}
.area svg{display:block;margin:0 auto}
.area h3{margin-top:18px;font-family:'Montserrat',sans-serif;font-weight:700;font-size:15px;color:var(--ink)}
.area .rule{width:28px;height:3px;background:var(--ink);margin:12px auto 16px}
.area p{font-size:13px;line-height:19px;color:#444;padding:0 34px}

/* footer */
.site-footer{left:0;top:2558px;width:1200px;height:324px;background:var(--black);color:var(--white)}
.footer-brand{left:75px;top:100px;font-size:26px;color:var(--white)}
.footer-about{left:75px;top:150px;width:255px;font-size:11px;line-height:13px;color:#ddd;text-align:justify}
.footer-divider{top:82px;width:1px;height:170px;background:#777}
.footer-col h4{font-family:'Montserrat',sans-serif;font-weight:500;font-size:17px;letter-spacing:.5px;padding-bottom:8px;border-bottom:1px solid #555;margin-bottom:18px;display:inline-block;padding-right:30px}
.links li{list-style:none;font-size:14px;line-height:26px;color:#eee}
.links li::before{content:"‹";margin-right:10px}
.contact-line{font-size:11.5px;line-height:16px;color:#eee}
.contact-row{display:flex;align-items:center;gap:10px;font-size:11.5px;color:#eee;height:23px}
.socials{display:flex;gap:4px}
.socials span{width:26px;height:26px;border-radius:50%;background:var(--white);display:block}
.call h5{font-family:'Montserrat',sans-serif;font-weight:600;font-size:16px}
.call .num{font-family:'Montserrat',sans-serif;font-weight:700;font-size:21px;letter-spacing:.5px}
.copyright{left:0;top:2882px;width:1200px;height:55px;background:var(--bar);color:#bbb;font-size:14px;text-align:center;line-height:55px}
</style>
</head>
<body>

<header class="site-header abs">
  <div class="brand abs">LEXMORE COUNSEL</div>
  <nav class="main-nav abs">
    <a class="active" href="#">HOME</a>
    <a href="#">ABOUT US</a>
    <a href="#">OUR PEOPLE</a>
    <a href="#">SERVICES</a>
    <a href="#">CONTACT US</a>
  </nav>
</header>

<section class="hero abs" role="img" aria-label="Team of smiling lawyers in business suits standing in front of an office building">
  <svg class="hero-arrow abs" style="left:54px" width="36" height="60" viewBox="0 0 36 60"><path d="M30 4 L6 30 L30 56" fill="none" stroke="#fff" stroke-width="4"/></svg>
  <svg class="hero-arrow abs" style="left:1110px" width="36" height="60" viewBox="0 0 36 60"><path d="M6 4 L30 30 L6 56" fill="none" stroke="#fff" stroke-width="4"/></svg>
  <div class="hero-title abs">GET YOUR LEGAL ADVICE<br>PROTECT YOU &amp; YOUR BUSINESS</div>
  <div class="hero-sub abs">Lorem ipsum dolor sit amet, consectetuer adipiscing elit.</div>
</section>

<div class="about-photo abs" role="img" aria-label="Businesswoman with folded arms in front of colleagues in a meeting"></div>
<div class="about-text abs">
  <h2>ABOUT US</h2>
  <p>Lorem ipsum dolor sit amet, consectetur adipiscing elit. Quid autem habent admirationis, cum prope accesseris? An hoc usque quaque, aliter in vita? Non igitur de improbo, sed de callido improbo quaerimus, qualis Q. Nam quibus rebus efficiuntur voluptates, eae non sunt in potestate sapientis. Negare non possum. Huic mori optimum esse propter desperationem sapientiae, illi propter spem vivere. Quid enim me prohiberet Epicureum esse, si probarem, quae ille diceret? Qui-vere falsone, quaerere mittimus-dicitur oculis se privasse;</p>
  <p>Varietates autem iniurasque fortunae facile veteres philosophorum praecepta instituta vita superabat. Et quod est munus, quod opus sapientiae? Non modo carum sibi quemque, verum etiam vehementer carum esse? Tu enim ista lenius, hic Stoicorum more nos vexat. Collatio igitur ista te nihil iuvat. Videamus animi partes, quarum est conspectus illustrior;</p>
  <span class="btn-more">Read More</span>
</div>

<section class="people abs">
  <h2 class="section-title abs" style="top:55px">OUR PEOPLE</h2>
  <p class="section-lead abs" style="top:98px">Lorem ipsum dolor sit amet, consectetur adipiscing elit. Quid autem habent admirationis, cum prope accesseris? An hoc usque quaque, aliter in vita? Non igitur de improbo, sed de callido improbo quaerimus, qualis Q. Nam quibus rebus efficiuntur voluptates, eae non sunt in potestate sapientis. Negare non possum. Huic mori optimum esse propter desperationem sapientiae, illi propter spem vivere. Quid enim me prohiberet Epicureum esse, si probarem, quae ille diceret? Qui-vere falsone, quaerere mittimus-dicitur oculis se privasse;</p>
  <div class="person abs" style="left:137px;top:195px">
    <div class="photo" role="img" aria-label="Portrait of a smiling founder in a light blue shirt" style="background:linear-gradient(160deg,#c9cfd8,#8f9bb0)"></div>
    <div class="name">Nora Whitfield</div><div class="role">Founder</div>
  </div>
  <div class="person abs" style="left:461px;top:195px">
    <div class="photo" role="img" aria-label="Portrait of a grey-haired founder in a suit and tie" style="background:linear-gradient(160deg,#b9bcc2,#6e737c)"></div>
    <div class="name" style="margin-top:16px">Dorian Vale</div><div class="role">Founder</div>
  </div>
  <div class="person abs" style="left:786px;top:195px">
    <div class="photo" role="img" aria-label="Portrait of a founder in a dark blazer leaning on a railing" style="background:linear-gradient(160deg,#aeb8c4,#4f5866)"></div>
    <div class="name" style="margin-top:16px">Clara Ostrow</div><div class="role">Founder</div>
  </div>
</section>

<h2 class="section-title abs" style="top:1828px">PRACTICE AREAS</h2>
<p class="section-lead abs" style="top:1870px">Lorem ipsum dolor sit amet, consectetur adipiscing elit. Quid autem habent admirationis, cum prope accesseris? An hoc usque quaque, aliter in vita? Non igitur de improbo, sed de callido improbo quaerimus, qualis Q. Nam quibus rebus efficiuntur voluptates, eae non sunt in potestate sapientis. Negare non possum. Huic mori optimum esse propter desperationem sapientiae, illi propter spem vivere. Quid enim me prohiberet Epicureum esse, si probarem.</p>

<div class="area abs" style="left:121px;top:1960px">
  <svg width="44" height="44" viewBox="0 0 44 44" fill="#111"><circle cx="17" cy="9" r="6"/><circle cx="30" cy="14" r="4"/><path d="M8 40 V26 a9 9 0 0 1 18 0 V40z"/><path d="M24 40 V27 a6 6 0 0 1 12 0 V40z"/><rect x="5" y="40" width="34" height="3"/></svg>
  <h3>FAMILY LAW</h3><div class="rule"></div>
  <p>Lorem ipsum dolor sit amet, consectetur adipiscing elit. Quid autem habent admirationis, cum</p>
</div>
<div class="area abs" style="left:356px;top:1960px">
  <svg width="44" height="44" viewBox="0 0 44 44"><circle cx="22" cy="22" r="19" fill="none" stroke="#111" stroke-width="2.5"/><text x="22" y="30" text-anchor="middle" font-family="Montserrat,sans-serif" font-weight="700" font-size="22" fill="#111">$</text></svg>
  <h3>DEBT RECOVERY</h3><div class="rule"></div>
  <p>Lorem ipsum dolor sit amet, consectetur adipiscing elit. Quid autem habent admirationis, cum</p>
</div>
<div class="area abs" style="left:591px;top:1960px">
  <svg width="44" height="44" viewBox="0 0 44 44" fill="none" stroke="#111" stroke-width="2.5"><rect x="14" y="4" width="16" height="18"/><path d="M18 10h8M18 15h8"/><path d="M4 30 l10-4 h12 a3 3 0 0 1 0 6 h-8 M18 32 h12 l8-6 M4 40 l8-2 h18 l10-10"/></svg>
  <h3>LEASES</h3><div class="rule"></div>
  <p>Lorem ipsum dolor sit amet, consectetur adipiscing elit. Quid autem habent admirationis, cum</p>
</div>
<div class="area abs" style="left:826px;top:1960px">
  <svg width="44" height="44" viewBox="0 0 44 44" fill="#111"><path d="M6 10 h32 v8 h-18 l-4 18 h-8 l3 -18 h-5z"/><rect x="30" y="6" width="4" height="4"/></svg>
  <h3>CRIMES &amp; TRAFFIC</h3><div class="rule"></div>
  <p>Lorem ipsum dolor sit amet, consectetur adipiscing elit. Quid autem habent admirationis, cum</p>
</div>

<div class="area abs" style="left:121px;top:2232px">
  <svg width="44" height="44" viewBox="0 0 44 44" fill="none" stroke="#111" stroke-width="2.5"><rect x="10" y="4" width="24" height="36" rx="3"/><path d="M15 12h14M15 18h14M15 24h14M15 30h10"/></svg>
  <h3>WILLS</h3><div class="rule"></div>
  <p>Lorem ipsum dolor sit amet, consectetur adipiscing elit. Quid autem habent admirationis, cum</p>
</div>
<div class="area abs" style="left:356px;top:2232px">
  <svg width="44" height="44" viewBox="0 0 44 44" fill="none" stroke="#111" stroke-width="3"><path d="M6 6 L32 32 M38 6 L12 32 M26 36 l10 -10 M8 26 l10 10 M34 34 l6 6 M10 34 l-6 6"/></svg>
  <h3>VIOLENCE</h3><div class="rule"></div>
  <p>Lorem ipsum dolor sit amet, consectetur adipiscing elit. Quid autem habent admirationis, cum</p>
</div>
<div class="area abs" style="left:591px;top:2232px">
  <svg width="44" height="44" viewBox="0 0 44 44" fill="none" stroke="#111" stroke-width="2.5"><rect x="6" y="4" width="26" height="36"/><path d="M11 12h16M11 18h12M11 24h8"/><path d="M24 36 l14 -16 l3 3 l-14 16 h-3z" fill="#111"/></svg>
  <h3>PROBATE TITLES</h3><div class="rule"></div>
  <p>Lorem ipsum dolor sit amet, consectetur adipiscing elit. Quid autem habent admirationis, cum</p>
</div>
<div class="area abs" style="left:826px;top:2232px">
  <svg width="44" height="44" viewBox="0 0 44 44" fill="#111"><path d="M24 6 a16 16 0 1 0 12 28 a13 13 0 1 1 -12 -28z"/><path d="M32 10 l1.8 4.5 4.7 .3 -3.7 3 1.2 4.6 -4 -2.6 -4 2.6 1.2 -4.6 -3.7 -3 4.7 -.3z"/></svg>
  <h3>SHARIAH LAW</h3><div class="rule"></div>
  <p>Lorem ipsum dolor sit amet, consectetur adipiscing elit. Quid autem habent admirationis, cum</p>
</div>

<footer class="site-footer abs">
  <div class="footer-brand brand abs">LEXMORE COUNSEL</div>
  <p class="footer-about abs">Lorem ipsum dolor sit amet, consectetur adipiscing elit. Quid autem habent admirationis, cum prope accesseris? An hoc usque quaque, aliter in vita? Non igitur de improbo, sed de callido improbo quaerimus.</p>

  <div class="footer-divider abs" style="left:355px"></div>
  <div class="footer-divider abs" style="left:578px"></div>
  <div class="footer-divider abs" style="left:853px"></div>

  <div class="footer-col abs" style="left:393px;top:70px">
    <h4>QUICK LINKS</h4>
    <ul class="links"><li>Home</li><li>About us</li><li>Services</li><li>Our people</li><li>Contact us</li></ul>
  </div>

  <div class="footer-col abs" style="left:622px;top:70px">
    <h4>CONTACT</h4>
    <p class="contact-line">4720 Brindle Ave<br>Marlow Springs, IL 60999</p>
    <div style="margin-top:12px">
      <div class="contact-row"><svg width="12" height="12" viewBox="0 0 24 24" fill="#fff"><path d="M6 2 l4 5 -2 3 a14 14 0 0 0 6 6 l3 -2 5 4 -3 4 C9 22 2 15 2 5z"/></svg>555-204-7731</div>
      <div class="contact-row"><svg width="12" height="12" viewBox="0 0 24 24"><rect x="6" y="1" width="12" height="22" rx="2" fill="none" stroke="#fff" stroke-width="2.5"/></svg>555-318-0942</div>
      <div class="contact-row"><svg width="12" height="12" viewBox="0 0 24 24"><rect x="1" y="5" width="22" height="14" fill="#fff"/><path d="M1 5 l11 8 11-8" fill="none" stroke="#000" stroke-width="2"/></svg>hello@lexmorecounsel.example</div>
      <div class="contact-row"><svg width="12" height="12" viewBox="0 0 24 24" fill="none" stroke="#fff" stroke-width="2.5"><circle cx="12" cy="12" r="10"/><path d="M2 12h20M12 2c4 4 4 16 0 20M12 2c-4 4-4 16 0 20"/></svg>www.lexmorecounsel.example</div>
    </div>
  </div>

  <div class="footer-col abs" style="left:900px;top:70px">
    <h4 style="border:none;padding-bottom:0;margin-bottom:20px">FOLLOW US ON</h4>
    <div class="socials"><span></span><span></span><span></span><span></span><span></span></div>
    <div style="width:22px;height:2px;background:#fff;margin:28px 0 22px"></div>
    <div class="call"><h5>CALL US ON</h5><div class="num">555-204-7731</div></div>
  </div>
</footer>

<div class="copyright abs">© 2018 Lexmore Counsel &nbsp;|&nbsp; Privacy Policy &nbsp;|&nbsp; User Agreement</div>

</body>
</html>
```